a little bit like bulkhaven but selling small amounts of high end tech gear directly to customers inbox.

Hi Designers,

I have had my artflockly logo attached to this project.
I have another web site (coolrivet.com.au)which will be dedicated mostly to
enthusiast,s that want to water cool their pc's. It's not quite finished. I may
need your help with that one once we get Gizpellbin up and running .I
like Rig Shelf Depot layout for Coolrivet
I want Giz pell to be simple to navigate, and similar to Bulkhaven.
I will be selling Enthusiast PC Components in small volumes ie first in
best dressed. weekly specials,daily specials,free shipping
There should be the ability for me to upload the component photo direct
from my Orbix5 Phone .
Links to the manufacturers website and product reviews from youtube
I will give you more in depth details tomorrow.
Updates

I would like my new site to be similar to q-Volt.com.au but cooler! Added Sunday, October 1, 2017

Target Market(s)

Enthusiast PC Builders

Industry/Entity Type

Tech

Coding

Coded - Design and coding required

Number of Pages Required

1 page

Font styles to use
Sans Serif

Colors
33b8a4

Requirements
Must have
• Link the price of my product to pricorn.com.au
• Drop down menus

```html
<!DOCTYPE html>
<html lang="en">
<head>
<meta charset="utf-8">
<title>Gizpellbin – Enthusiast PC Components</title>
<link href="https://fonts.googleapis.com/css2?family=Open+Sans:wght@400;600;700&family=Roboto+Condensed:wght@400;700&display=swap" rel="stylesheet">
<style>
:root{
  --teal:#33b8a4;
  --teal-dark:#2a9d8b;
  --navy:#1f5273;
  --ink:#333333;
  --text:#555555;
  --muted:#8a8a8a;
  --line:#e2e2e2;
  --bar:#353535;
  --panel:#f0f0f0;
  --grey-band:#6b6b6b;
  --white:#ffffff;
  --star:#f2a71b;
}
*{box-sizing:border-box;margin:0;padding:0}
html,body{width:1200px;height:2889px;overflow:hidden}
body{font-family:"Open Sans",Arial,sans-serif;color:var(--text);background:var(--white);position:relative}
.page{position:relative;width:1200px;height:2889px}
a{color:inherit;text-decoration:none}

/* header */
.brand{position:absolute;left:100px;top:30px;display:flex;align-items:center;gap:12px}
.brand-mark{width:44px;height:44px;border-radius:50%;background:var(--navy)}
.brand-name{font-weight:700;font-size:34px;color:var(--navy);letter-spacing:-.5px}
.utility{position:absolute;right:100px;top:38px;display:flex;align-items:center;gap:22px;font-size:12px;color:var(--ink);text-transform:uppercase}
.utility span{display:flex;align-items:center;gap:7px}
.utility svg{width:15px;height:15px}
.utility .phone{font-size:17px;font-weight:600;color:var(--navy);text-transform:none}
.main-nav{position:absolute;right:100px;top:98px;display:flex;gap:36px;font-size:13px;color:var(--ink);text-transform:uppercase}
.main-nav .active{color:var(--navy)}

/* dark tool bar */
.toolbar{position:absolute;left:0;top:150px;width:1200px;height:55px;background:var(--bar)}
.cat-toggle{position:absolute;left:100px;top:0;width:218px;height:55px;background:var(--navy);display:flex;align-items:center;color:var(--white);font-family:"Roboto Condensed",sans-serif;font-weight:700;font-size:16px}
.cat-toggle .burger{width:55px;height:55px;background:rgba(0,0,0,.15);display:flex;align-items:center;justify-content:center;margin-right:20px}
.search{position:absolute;left:343px;top:9px;width:512px;height:37px;background:var(--white);display:flex;align-items:center;font-size:11px}
.search .field{flex:1;padding-left:16px;color:var(--ink)}
.search .scope{width:130px;height:100%;border-left:1px solid var(--line);display:flex;align-items:center;justify-content:center;gap:6px;color:var(--ink);font-size:10px}
.search .go{width:44px;height:100%;border-left:1px solid var(--line);display:flex;align-items:center;justify-content:center}
.cart{position:absolute;left:900px;top:0;width:200px;height:55px;background:var(--navy);color:var(--white);display:flex;align-items:center;gap:14px;padding-left:22px;font-size:13px}

/* sidebar */
.categories{position:absolute;left:100px;top:205px;width:218px;height:1075px;border:1px solid var(--line);border-top:none;list-style:none}
.categories li{height:37.5px;border-bottom:1px solid var(--line);display:flex;align-items:center;padding-left:18px;font-size:11px;color:var(--ink)}
.categories li::before{content:"";width:4px;height:4px;border-radius:50%;background:var(--muted);margin-right:12px}

/* hero */
.hero{position:absolute;left:343px;top:229px;width:757px;height:426px;background:linear-gradient(180deg,#0f2230 0%,#1d4156 45%,#2f6a7e 70%,#142b38 100%);overflow:hidden}
.hero h1{position:absolute;top:50px;width:100%;text-align:center;font-family:"Roboto Condensed",sans-serif;font-weight:700;font-size:50px;color:var(--white);letter-spacing:1px}
.hero p{position:absolute;top:118px;width:100%;text-align:center;font-family:"Roboto Condensed",sans-serif;font-weight:700;font-size:15px;line-height:22px;color:var(--white)}
.slide-arrow{position:absolute;top:213px;width:28px;height:28px;border:1px solid rgba(255,255,255,.7);border-radius:50%;display:flex;align-items:center;justify-content:center}

/* promos */
.promo{position:absolute;top:680px;width:372px;height:170px;overflow:hidden}
.promo .photo{position:absolute;right:0;top:0;width:58%;height:100%}
.promo .wash{position:absolute;left:0;top:0;width:100%;height:100%;background:linear-gradient(100deg,var(--teal) 0%,var(--teal) 42%,rgba(51,184,164,0) 70%)}
.promo .label{position:absolute;left:20px;top:20px;color:var(--white);font-family:"Roboto Condensed",sans-serif}
.promo small{display:block;font-size:14px;font-weight:700}
.promo strong{display:block;font-size:20px;font-weight:400;margin-top:6px}
.promo .btn{position:absolute;left:20px;top:80px;background:#2c2c2c;color:var(--white);font-size:11px;padding:7px 14px}

/* section heads */
.plain-head{position:absolute;left:341px;top:885px;width:759px;display:flex;justify-content:space-between;align-items:center}
.plain-head h2{font-family:"Roboto Condensed",sans-serif;font-weight:400;font-size:24px;color:var(--ink)}
.pager{display:flex;gap:5px}
.pager span{width:24px;height:24px;border:1px solid #bdbdbd;border-radius:50%;display:flex;align-items:center;justify-content:center;background:var(--white)}
.pager svg{width:9px;height:9px}

.weekly{position:absolute;left:343px;top:945px;width:757px;height:335px;display:flex;justify-content:space-between}
.weekly .card{width:230px;border:1px solid var(--line)}

.block{position:absolute;left:100px;width:1000px;height:410px;border:1px solid var(--line)}
.block-head{height:44px;background:var(--panel);display:flex;align-items:center;justify-content:space-between;padding-right:12px}
.block-head .title{display:flex;align-items:center;gap:14px;font-family:"Roboto Condensed",sans-serif;font-size:20px;color:var(--ink);text-transform:uppercase}
.block-head .badge{width:58px;height:44px;background:var(--teal);display:flex;align-items:center;justify-content:center}
.block-head .badge i{width:26px;height:26px;border-radius:50%;background:var(--white);display:block}
.block-row{display:flex;height:364px}
.block-row .card{flex:1;border-right:1px solid var(--line);position:relative;overflow:hidden}
.block-row .card:last-child{border-right:none}

/* product card */
.card{text-align:center;background:var(--white);padding-top:8px}
.card .shot{width:calc(100% - 16px);height:184px;margin:0 auto;border-radius:2px}
.block .card .shot{width:170px;height:140px;margin-top:22px;border-radius:4px}
.stars{margin-top:14px;font-size:10px;letter-spacing:1px;color:#cfcfcf}
.stars b{color:var(--star);font-weight:400}
.card .name{font-size:12.5px;line-height:19px;color:var(--ink);margin:14px 32px 0}
.weekly .card .name{margin:16px 22px 0}
.card .price{margin-top:8px;font-size:17px}
.card .price .now{color:var(--teal);font-weight:600}
.card .price .was{color:var(--ink);font-size:13px;font-weight:600}
.card .price .was s{text-decoration:line-through}
.card .add{display:inline-block;margin-top:10px;border:1px solid #bdbdbd;font-size:11px;color:var(--ink);padding:5px 14px;text-transform:uppercase}
.ribbon{position:absolute;left:-30px;top:14px;width:110px;transform:rotate(-45deg);background:var(--teal);color:var(--white);font-size:10px;text-align:center;padding:3px 0;z-index:1}

/* shipping + newsletter */
.promo-band{position:absolute;left:0;top:2315px;width:1200px;height:188px;background:var(--grey-band);overflow:hidden}
.promo-band .teal{position:absolute;left:0;top:0;width:100%;height:100%}
.ship{position:absolute;left:96px;top:38px;color:var(--white);font-family:"Roboto Condensed",sans-serif}
.ship strong{display:block;font-size:40px;line-height:38px;font-weight:700;letter-spacing:1px}
.ship small{display:block;font-size:19px;margin-top:6px;font-weight:700;letter-spacing:.5px}
.truck{position:absolute;left:395px;top:45px}
.news{position:absolute;left:666px;top:45px;color:var(--white)}
.news h3{font-family:"Roboto Condensed",sans-serif;font-weight:400;font-size:24px}
.news .form{margin-top:20px;width:434px;height:44px;background:var(--white);display:flex;align-items:center;justify-content:space-between;padding:0 6px 0 16px;font-size:12px;color:var(--text)}
.news .form span.btn{background:#222;color:var(--white);font-weight:700;font-size:12px;padding:9px 16px}

/* footer */
.footer-brand{position:absolute;left:100px;top:2555px;width:260px}
.footer-brand .brand-row{display:flex;align-items:center;gap:12px}
.footer-brand p{margin-top:30px;font-size:11px;line-height:21px;color:var(--ink)}
.foot-col{position:absolute;top:2580px}
.foot-col h4{font-family:"Roboto Condensed",sans-serif;font-weight:400;font-size:19px;color:var(--ink);text-transform:uppercase;margin-bottom:22px}
.foot-col li{list-style:none;font-size:11px;color:var(--ink);line-height:26px}
.contact-line{display:flex;gap:14px;font-size:12px;color:var(--ink);line-height:17px;margin-bottom:14px}
.contact-line svg{flex:none;margin-top:2px}

.bottom{position:absolute;left:0;top:2810px;width:1200px;height:79px;background:var(--panel)}
.social{position:absolute;left:100px;top:28px;display:flex;gap:6px}
.social i{width:20px;height:20px;border:1px solid #9a9a9a;border-radius:50%;display:block}
.copy{position:absolute;left:0;width:100%;top:34px;text-align:center;font-size:11px;color:var(--ink)}
.pay{position:absolute;right:100px;top:27px;display:flex;gap:6px}
.pay i{width:38px;height:24px;background:var(--white);border:1px solid #d6d6d6;border-radius:2px;display:block}
</style>
</head>
<body>
<div class="page">

<header>
  <div class="brand"><span class="brand-mark"></span><span class="brand-name">Gizpellbin</span></div>
  <div class="utility">
    <span><svg viewBox="0 0 16 16"><rect x="2" y="3" width="11" height="11" fill="none" stroke="#555" stroke-width="1.5"/><path d="M7 9l7-7" stroke="#555" stroke-width="1.5"/></svg>Register</span>
    <span><svg viewBox="0 0 16 16"><path d="M8 2h6v12H8" fill="none" stroke="#555" stroke-width="1.5"/><path d="M1 8h9M7 5l3 3-3 3" fill="none" stroke="#555" stroke-width="1.5"/></svg>Login</span>
    <span><svg viewBox="0 0 16 16"><circle cx="8" cy="5" r="3.5" fill="#555"/><path d="M1 16c0-5 14-5 14 0z" fill="#555"/></svg>My Account</span>
    <span><svg viewBox="0 0 16 16"><path d="M0 2h3l2 8h9l2-6H4" fill="none" stroke="#555" stroke-width="1.5"/><circle cx="6" cy="13" r="1.4" fill="#555"/><circle cx="13" cy="13" r="1.4" fill="#555"/></svg>My Cart</span>
    <span class="phone"><svg viewBox="0 0 16 16"><rect x="4" y="1" width="8" height="14" rx="1.5" fill="#1f5273"/></svg>0800 41 27 53</span>
  </div>
  <nav class="main-nav">
    <a class="active">Home</a><a>Reward Points</a><a>Next Day Dispatch</a><a>Coupon Codes</a><a>Contact Us</a>
  </nav>
</header>

<div class="toolbar">
  <div class="cat-toggle"><span class="burger"><svg width="18" height="14"><path d="M0 1h18M0 7h18M0 13h18" stroke="#fff" stroke-width="2"/></svg></span>CATEGORIES</div>
  <div class="search">
    <span class="field">Search Here</span>
    <span class="scope">ALL CATEGORIES <svg width="8" height="6"><path d="M1 1l3 3 3-3" fill="none" stroke="#333" stroke-width="1.3"/></svg></span>
    <span class="go"><svg width="13" height="13"><circle cx="5.5" cy="5.5" r="4" fill="none" stroke="#d03a3a" stroke-width="1.8"/><path d="M8.5 8.5l3.5 3.5" stroke="#d03a3a" stroke-width="1.8"/></svg></span>
  </div>
  <div class="cart"><svg width="22" height="20"><path d="M0 2h4l3 10h11l3-8H6" fill="none" stroke="#fff" stroke-width="2"/><circle cx="8" cy="16" r="2" fill="#fff"/><circle cx="17" cy="16" r="2" fill="#fff"/></svg>0 ITEM(S) - $0.00</div>
</div>

<ul class="categories">
  <li>NEW ARRIVAL</li><li>CLEARANCE</li><li>Barebone System</li><li>Build Your Own</li><li>Cables/ Adaptors</li><li>CD/ DVD Drives</li><li>Computer Case/ PSU</li><li>Computer System</li><li>Consumable/ FDD</li><li>Cooling/ PC Mod</li><li>CPU/ Processor</li><li>Digital Photo Frame</li><li>Digital/ Web Camera</li><li>Dot Matrix Printer</li><li>Electrical</li><li>Firewire/ SCSI/ USB</li><li>Flash Memory</li><li>Hard Disk/ Storage</li><li>HDD Enclosure</li><li>Ink/ Toner</li><li>Inkjet Printer</li><li>Keyboard/ Mouse</li><li>KVM Switches</li><li>Laser Printer</li><li>Memory/ Ram</li><li>Mobile Phone</li><li>Modem/ ADSL/ VOIP</li><li>TV Tuner/ Capture</li>
</ul>

<section class="hero" role="img" aria-label="Close-up photo of a glowing circuit board with chips">
  <h1>ENTHUSIAST PC</h1>
  <p>SED UT PERSPICIATIS UNDE OMNIS ISTE NATUS<br>ERROR SIT VOLUPTATEM</p>
  <span class="slide-arrow" style="left:16px"><svg width="8" height="10"><path d="M6 1L2 5l4 4" fill="none" stroke="#fff" stroke-width="1.5"/></svg></span>
  <span class="slide-arrow" style="right:16px"><svg width="8" height="10"><path d="M2 1l4 4-4 4" fill="none" stroke="#fff" stroke-width="1.5"/></svg></span>
</section>

<div class="promo" style="left:343px">
  <div class="photo" role="img" aria-label="Photo of blue network cables" style="background:linear-gradient(160deg,#4f86ad,#9cc0d4)"></div>
  <div class="wash"></div>
  <div class="label"><small>SHOP FOR</small><strong>CABLES/ ADAPTORS</strong></div>
  <span class="btn">VIEW ALL</span>
</div>
<div class="promo" style="left:728px">
  <div class="photo" role="img" aria-label="Photo of a rack of computer systems" style="background:linear-gradient(160deg,#4a5866,#9aa8b4)"></div>
  <div class="wash"></div>
  <div class="label"><small>SHOP FOR</small><strong>COMPUTER SYSTEM</strong></div>
  <span class="btn">VIEW ALL</span>
</div>

<div class="plain-head">
  <h2>WEEKLY SPECIALS</h2>
  <div class="pager"><span><svg viewBox="0 0 10 10"><path d="M7 1L3 5l4 4" fill="none" stroke="#888" stroke-width="1.5"/></svg></span><span><svg viewBox="0 0 10 10"><path d="M3 1l4 4-4 4" fill="none" stroke="#888" stroke-width="1.5"/></svg></span></div>
</div>
<section class="weekly">
  <article class="card"><div class="shot" role="img" aria-label="Green circuit board product photo" style="background:linear-gradient(180deg,#eef1ee,#cfdccf)"></div><p class="name">Sed ut perspiciatis unde omnis iste natus error sit</p><p class="price"><span class="now">$50.99</span> <span class="was">- <s>$100.99</s></span></p><span class="add">Add to Cart</span></article>
  <article class="card"><div class="shot" role="img" aria-label="Desktop computer and peripherals product photo" style="background:linear-gradient(180deg,#eff0f2,#d3d7dd)"></div><p class="name">Sed ut perspiciatis unde omnis iste natus error sit</p><p class="price"><span class="now">$50.99</span> <span class="was">- <s>$100.99</s></span></p><span class="add">Add to Cart</span></article>
  <article class="card"><div class="shot" role="img" aria-label="Assorted PC components product photo" style="background:linear-gradient(180deg,#eff0f2,#d2d8e2)"></div><p class="name">Sed ut perspiciatis unde omnis iste natus error sit</p><p class="price"><span class="now">$50.99</span> <span class="was">- <s>$100.99</s></span></p><span class="add">Add to Cart</span></article>
</section>

<section class="block" style="top:1343px">
  <div class="block-head">
    <div class="title"><span class="badge"><i></i></span>Best Dressed</div>
    <div class="pager"><span><svg viewBox="0 0 10 10"><path d="M7 1L3 5l4 4" fill="none" stroke="#888" stroke-width="1.5"/></svg></span><span><svg viewBox="0 0 10 10"><path d="M3 1l4 4-4 4" fill="none" stroke="#888" stroke-width="1.5"/></svg></span></div>
  </div>
  <div class="block-row">
    <article class="card"><div class="shot" role="img" aria-label="Motherboard product photo" style="background:linear-gradient(180deg,#f2f2f3,#d9dadc)"></div><p class="stars"><b>★★★</b>★★</p><p class="name">Sed ut perspiciatis unde omnis iste natus error sit</p><p class="price"><span class="now">$50.99</span> <span class="was">- <s>$100.99</s></span></p><span class="add">Add to Cart</span></article>
    <article class="card"><span class="ribbon">Sale</span><div class="shot" role="img" aria-label="Processor chip product photo" style="background:linear-gradient(180deg,#f3f4f5,#dee1e3)"></div><p class="stars"><b>★★★</b>★★</p><p class="name">Sed ut perspiciatis unde omnis iste natus error sit</p><p class="price"><span class="now">$50.99</span> <span class="was">- <s>$100.99</s></span></p><span class="add">Add to Cart</span></article>
    <article class="card"><div class="shot" role="img" aria-label="Motherboard with red slots product photo" style="background:linear-gradient(180deg,#f4f2f2,#e1d8d8)"></div><p class="stars"><b>★★★</b>★★</p><p class="name">Sed ut perspiciatis unde omnis iste natus error sit</p><p class="price"><span class="now">$50.99</span> <span class="was">- <s>$100.99</s></span></p><span class="add">Add to Cart</span></article>
    <article class="card"><span class="ribbon">Sale</span><div class="shot" role="img" aria-label="Laptop product photo" style="background:linear-gradient(180deg,#f2f3f4,#d8dbdf)"></div><p class="stars"><b>★★★</b>★★</p><p class="name">Sed ut perspiciatis unde omnis iste natus error sit</p><p class="price"><span class="now">$50.99</span> <span class="was">- <s>$100.99</s></span></p><span class="add">Add to Cart</span></article>
  </div>
</section>

<section class="block" style="top:1814px">
  <div class="block-head">
    <div class="title"><span class="badge"><i></i></span>Daily Specials</div>
    <div class="pager"><span><svg viewBox="0 0 10 10"><path d="M7 1L3 5l4 4" fill="none" stroke="#888" stroke-width="1.5"/></svg></span><span><svg viewBox="0 0 10 10"><path d="M3 1l4 4-4 4" fill="none" stroke="#888" stroke-width="1.5"/></svg></span></div>
  </div>
  <div class="block-row">
    <article class="card"><div class="shot" role="img" aria-label="Compact motherboard product photo" style="background:linear-gradient(180deg,#f2f2f3,#d9dadc)"></div><p class="stars"><b>★★★</b>★★</p><p class="name">Sed ut perspiciatis unde omnis iste natus error sit</p><p class="price"><span class="now">$50.99</span> <span class="was">- <s>$100.99</s></span></p><span class="add">Add to Cart</span></article>
    <article class="card"><span class="ribbon">20% Save</span><div class="shot" role="img" aria-label="Green expansion board product photo" style="background:linear-gradient(180deg,#f1f3f0,#d7e0d5)"></div><p class="stars"><b>★★★</b>★★</p><p class="name">Sed ut perspiciatis unde omnis iste natus error sit</p><p class="price"><span class="now">$50.99</span> <span class="was">- <s>$100.99</s></span></p><span class="add">Add to Cart</span></article>
    <article class="card"><div class="shot" role="img" aria-label="Drive with ribbon cable product photo" style="background:linear-gradient(180deg,#f4f2f0,#e2dad3)"></div><p class="stars"><b>★★★</b>★★</p><p class="name">Sed ut perspiciatis unde omnis iste natus error sit</p><p class="price"><span class="now">$50.99</span> <span class="was">- <s>$100.99</s></span></p><span class="add">Add to Cart</span></article>
    <article class="card"><span class="ribbon">20% Save</span><div class="shot" role="img" aria-label="Display module board product photo" style="background:linear-gradient(180deg,#f0f2f5,#d5dbe6)"></div><p class="stars"><b>★★★</b>★★</p><p class="name">Sed ut perspiciatis unde omnis iste natus error sit</p><p class="price"><span class="now">$50.99</span> <span class="was">- <s>$100.99</s></span></p><span class="add">Add to Cart</span></article>
  </div>
</section>

<section class="promo-band">
  <svg class="teal" viewBox="0 0 1200 188" preserveAspectRatio="none"><polygon points="0,0 665,0 605,188 0,188" fill="#33b8a4"/></svg>
  <div class="ship"><strong>FREE<br>SHIPPING</strong><small>WE ALWAYS GUARANTEE</small></div>
  <svg class="truck" width="140" height="90" viewBox="0 0 140 90">
    <path d="M0 22h30M6 38h24M12 54h18" stroke="#fff" stroke-width="5" stroke-linecap="round"/>
    <rect x="38" y="8" width="62" height="56" rx="4" fill="#fff"/>
    <path d="M100 24h20l16 20v20h-36z" fill="#fff"/>
    <path d="M106 30h12l10 13h-22z" fill="#33b8a4"/>
    <circle cx="58" cy="70" r="11" fill="#fff" stroke="#33b8a4" stroke-width="5"/>
    <circle cx="118" cy="70" r="11" fill="#fff" stroke="#33b8a4" stroke-width="5"/>
  </svg>
  <div class="news">
    <h3>NEWSLETTER SIGN UP</h3>
    <div class="form"><span>Enter Email Address</span><span class="btn">SIGN UP</span></div>
  </div>
</section>

<footer>
  <div class="footer-brand">
    <div class="brand-row"><span class="brand-mark"></span><span class="brand-name">Gizpellbin</span></div>
    <p>Sed ut perspiciatis unde omnis iste natus error sit voluptatem accusantium doloremque laudantium, totam rem aperiam, eaque ipsa quae ab</p>
  </div>
  <div class="foot-col" style="left:449px">
    <h4>Contact Us</h4>
    <div class="contact-line"><svg width="12" height="16"><path d="M6 0a6 6 0 0 1 6 6c0 4-6 10-6 10S0 10 0 6a6 6 0 0 1 6-6z" fill="#1f5273"/><circle cx="6" cy="6" r="2.2" fill="#fff"/></svg><span style="font-size:11px">Gizpellbin<br>Lindenweg Str. 27 &nbsp;50321 Brühlingen<br>Germany</span></div>
    <div class="contact-line"><svg width="14" height="14"><path d="M3 1l3 3-2 2c1 2 2 3 4 4l2-2 3 3-2 2C6 13 1 8 1 3z" fill="#1f5273"/></svg><span>Phone: +49-221-47-15-302</span></div>
    <div class="contact-line"><svg width="14" height="12"><rect width="14" height="11" fill="#1f5273"/><path d="M0 0l7 6 7-6" fill="none" stroke="#fff" stroke-width="1.3"/></svg><span>Email: mail@Gizpellbin.com.au</span></div>
  </div>
  <div class="foot-col" style="left:758px">
    <h4>Customer Service</h4>
    <ul><li>About Us</li><li>Term &amp; Condition of Use</li><li>Term &amp; Condition of Sale</li><li>Privacy Statement</li><li>Affiliates</li></ul>
  </div>
  <div class="foot-col" style="left:994px">
    <h4>Quick Links</h4>
    <ul><li>My Account</li><li>Order History</li><li>Wishlist</li><li>Returns</li><li>Freight Policy</li></ul>
  </div>
  <div class="bottom">
    <div class="social"><i></i><i></i><i></i><i></i></div>
    <p class="copy">©2017 &nbsp;Gizpellbin. All Rights Reserved.</p>
    <div class="pay"><i></i><i></i><i></i><i></i></div>
  </div>
</footer>

</div>
</body>
</html>
```